Office brochure for chronic pain doctor

I need an brochure for my office, and since I want to be able to mail the brochure, I think trifold would be the best size. I treat patients with chronic head and neck pain, as well as sleep apnea. I treat all of the following:

1. headaches
2. myofascial pain, which is a fancy way of saying muscle pain
3. neuropathic pain, which is a fancy way of saying nerve pain
4. TMJ, which stands for the temporomandibular joint (jaw joint)
5. obstructive sleep apnea

The colors will be based on my logo on my website, which you can see at www.BrightJPR.net, and you can learn more about what I do at my website. JPR stands for orofacial pain, which is a speciality training within the field of dentistry but I do not treat teeth. I have high resolution graphics for the brochure so I need someone with an artistic eye to design and lay out the brochure.

The logo colors are:
Purple 9e80bb
Pink f6b1d0
Blue 0f4b8f
Updates

I had a request for the logo in a .ai or .pdf format, which I have just uploaded. Please let me know if you have any other requests. Thank you, Dale

Target Market(s)

80% female, 20% male. I am in an upscale area of Los Angeles called Beverly Hills but I will see a patient from any area around Los Angeles or from any area in the world.

Industry/Entity Type

Training

Colors
6b449b
e567a6
0355a3

Requirements
Must have
• I want a small section of the brochure to feature each of the five areas I treat, and I have included an image to place in each of the five sections. A small section should include a short bio of me, which you can condense from www.brightjpr.net/dale. The brochure must appeal to women since 80% of my patients are female but I don't want to completely ignore men. Most of the pain patients are female, and most of the sleep apnea patients are male.

Here are the colors in my logo
Purple 9e80bb
Pink f6b1d0
Blue 0f4b8f
Should not have
• Anything related to teeth or dentistry.
No decorative or script fonts.

```html
<!DOCTYPE html>
<html lang="en">
<head>
<meta charset="utf-8">
<title>Trifold Brochure – Inside Spread</title>
<link rel="stylesheet" href="https://fonts.googleapis.com/css2?family=Questrial&family=Jost:wght@400;500&display=swap">
<style>
  :root {
    --page-bg: #ffffff;
    --sheet-border: #c8c8c8;
    --fold-line: #8a8a8a;
    --label-grey: #8c8c8c;
    --navy: #0f3d6e;
    --navy-deep: #1f4a80;
    --mauve: #9b8fb0;
    --blush: #f2bfbe;
    --blush-box: rgba(241, 185, 184, 0.92);
    --rose-text: #f4b9c1;
    --white: #ffffff;
  }
  * { margin: 0; padding: 0; box-sizing: border-box; }
  html, body {
    width: 1200px; height: 1000px; overflow: hidden;
    background: var(--page-bg);
  }
  .canvas { position: relative; width: 1200px; height: 1000px; }

  .panel-label {
    position: absolute; top: 153px; width: 80px; margin-left: -40px;
    text-align: center; font: 11px "Questrial", sans-serif; color: var(--label-grey);
  }

  .sheet {
    position: absolute; left: 205px; top: 195px; width: 792px; height: 613px;
    border: 1px solid var(--sheet-border);
    background: linear-gradient(to bottom,
      var(--navy-deep) 0%, var(--mauve) 17%, var(--blush) 37%,
      #f5cdcb 48%, var(--white) 66%);
    overflow: hidden;
  }

  .fold {
    position: absolute; top: 8px; bottom: 0; width: 0;
    border-left: 1px dashed var(--fold-line); z-index: 3;
  }

  .intro {
    position: absolute; left: 8px; top: 8px; width: 460px; height: 207px;
    background: var(--blush-box); padding: 20px 12px 0 12px; color: var(--white);
    font-family: "Questrial", sans-serif;
  }
  .intro h1 { font-weight: 400; font-size: 21.5px; line-height: 26px; margin-bottom: 8px; }
  .intro p { font-size: 10.4px; line-height: 14.6px; margin-bottom: 14px; }

  .welcome {
    position: absolute; left: 509px; top: 34px; width: 254px;
    font-family: "Questrial", sans-serif;
  }
  .welcome .lead {
    color: var(--rose-text); font-size: 16px; line-height: 21.5px;
    text-align: justify; margin-bottom: 22px;
  }
  .welcome .note { color: var(--navy); font-size: 16px; line-height: 21px; }

  .topic {
    position: absolute; top: 233px; width: 146px;
    font-family: "Jost", sans-serif; color: var(--navy);
  }
  .topic-art { display: block; width: 146px; height: 167px; }
  .topic h2 {
    font-family: "Questrial", sans-serif; font-weight: 400;
    font-size: 12.5px; letter-spacing: 0.2px;
    text-align: center; margin: 10px 0 5px;
  }
  .topic p { font-size: 9.8px; line-height: 14.2px; text-align: justify; }
</style>
</head>
<body>
<div class="canvas">
  <div class="panel-label" style="left:313px">Panel 1</div>
  <div class="panel-label" style="left:595px">Panel 2</div>
  <div class="panel-label" style="left:850px">Panel 3</div>

  <div class="sheet">
    <div class="fold" style="left:265px"></div>
    <div class="fold" style="left:530px"></div>

    <section class="intro">
      <h1>Oliamiammii Riiichjsk Hikkdkdkdjlka</h1>
      <p>Um iriustrud tio cor sum estrud dolore tatem quat nim vel dolum zzril ullan utat am niat. Wis acip ercil ut ip ex eugue vulput num zzrit praesse niscili scipit do exerci molor ipit nis at, quissi tat aliquat. Ut vent lam, qucommy nulputet nulput in vel ute faci erat vel ea cor irit ute commod molor senisit eugiam velit venit num veiesquat volorpe riiisi.</p>
      <p>dolortin vel il digna cons dolobore commodo loreros tismodo loboree tumsan henisit, cortie tat. Ut ad magna faccumsan ulla core core dolortie modolore feu feugait luptat. iduiscil ilit</p>
    </section>

    <section class="welcome">
      <p class="lead">Are, ocavoctus haed auderdis cae adhuitus scidiis turbentem o rno iur, quam inerfin dit, vignpr aricesce noculocris</p>
      <p class="note">bonvoludem egil rum licia maris, dum o terur.</p>
    </section>

    <article class="topic" style="left:8px">
      <svg class="topic-art" role="img" aria-label="Illustration of a woman with headache pain highlighted on one side of the head" viewBox="0 0 146 167">
        <defs><linearGradient id="g1" x1="0" y1="0" x2="0" y2="1"><stop offset="0" stop-color="#efe4df"/><stop offset="1" stop-color="#e9c7b4"/></linearGradient></defs>
        <rect width="146" height="167" fill="url(#g1)"/>
      </svg>
      <h2>FDGSGHDKLKJD</h2>
      <p>It in utat nit, si eugiat, vel etum-mol oborem veliquismodo com-my nim nim in ulputat.<br>Ut ad doloboreetue tie duis augiamet prating et euismolor acinim venis ad min verci guero etumsan heniam niam vullamet, cons accum ex euguer iusci bla conullan elit nulputpatio com-modignis</p>
    </article>

    <article class="topic" style="left:166px">
      <svg class="topic-art" role="img" aria-label="Illustration of a reclining person showing the airway during sleep apnea" viewBox="0 0 146 167">
        <defs><linearGradient id="g2" x1="0" y1="0" x2="0" y2="1"><stop offset="0" stop-color="#ffffff"/><stop offset="0.55" stop-color="#e6c6b6"/><stop offset="1" stop-color="#a9a9a9"/></linearGradient></defs>
        <rect width="146" height="167" fill="url(#g2)"/>
      </svg>
      <h2>FDGSGHDKLKJD</h2>
      <p>It in utat nit, si eugiat, vel etum-mol oborem veliquismodo com-my nim nim in ulputat.<br>Ut ad doloboreetue tie duis augiamet prating et euismolor acinim venis ad min verci guero etumsan heniam niam vullamet, cons accum ex euguer iusci bla conullan elit nulputpatio com-modignis</p>
    </article>

    <article class="topic" style="left:323px">
      <svg class="topic-art" role="img" aria-label="Anatomical illustration of the jaw joint and surrounding muscles" viewBox="0 0 146 167">
        <defs><linearGradient id="g3" x1="0" y1="0" x2="1" y2="1"><stop offset="0" stop-color="#d9d2ad"/><stop offset="0.5" stop-color="#b8867a"/><stop offset="1" stop-color="#cfc8a6"/></linearGradient></defs>
        <rect width="146" height="167" fill="url(#g3)"/>
      </svg>
      <h2>FDGSGHDKLKJD</h2>
      <p>It in utat nit, si eugiat, vel etum-mol oborem veliquismodo com-my nim nim in ulputat.<br>Ut ad doloboreetue tie duis augiamet prating et euismolor acinim venis ad min verci guero etumsan heniam niam vullamet, cons accum ex euguer iusci bla conullan elit nulputpatio com-modignis</p>
    </article>

    <article class="topic" style="left:480px">
      <svg class="topic-art" role="img" aria-label="Anatomical illustration of head and neck muscles" viewBox="0 0 146 167">
        <defs><linearGradient id="g4" x1="0" y1="0" x2="0" y2="1"><stop offset="0" stop-color="#f4ece6"/><stop offset="0.5" stop-color="#b96a55"/><stop offset="1" stop-color="#9a3f2f"/></linearGradient></defs>
        <rect width="146" height="167" fill="url(#g4)"/>
      </svg>
      <h2>FDGSGHDKLKJD</h2>
      <p>It in utat nit, si eugiat, vel etum-mol oborem veliquismodo com-my nim nim in ulputat.<br>Ut ad doloboreetue tie duis augiamet prating et euismolor acinim venis ad min verci guero etumsan heniam niam vullamet, cons accum ex euguer iusci bla conullan elit nulputpatio com-modignis</p>
    </article>

    <article class="topic" style="left:638px">
      <svg class="topic-art" role="img" aria-label="Illustration of a woman's face mapping facial nerve pain regions" viewBox="0 0 146 167">
        <defs><linearGradient id="g5" x1="0" y1="0" x2="0" y2="1"><stop offset="0" stop-color="#f1e6e1"/><stop offset="0.6" stop-color="#e8c5b3"/><stop offset="1" stop-color="#fbf1ec"/></linearGradient></defs>
        <rect width="146" height="167" fill="url(#g5)"/>
      </svg>
      <h2>FDGSGHDKLKJD</h2>
      <p>It in utat nit, si eugiat, vel etum-mol oborem veliquismodo com-my nim nim in ulputat.<br>Ut ad doloboreetue tie duis augiamet prating et euismolor acinim venis ad min verci guero etumsan heniam niam vullamet, cons accum ex euguer iusci bla conullan elit nulputpatio com-modignis</p>
    </article>
  </div>
</div>
</body>
</html>
```